Etiketten-Design von Nahrungsergänzungsmitteln
Zielgruppe
Ich bin eine Privatperson (Kleinunternehmer). Vertrieb von Nahrungsergänzungsmitteln.
Unsere Zielgruppe betrifft den Sportbereich.
Genauer gesagt professionelle und Hobbyathleten im Fitness/Bodybuilding Sektor.
Aber auch in anderen Sportarten wird das Produkt genutzt.
Alter der Kunden zwischen 18 und 60 Jahren. (Für diese Produktkategorie hauptsächlich männlich)
Das Produktetikett sollte ein richtiger 'Eyecatcher' werden, bzw.
auch die Neugier der Kunden/Trainingsbegeisterten wecken.
Aufgabenstellung
Produktname im oberen Bereich des Etiketts angeführt werden.
Produktname: MARLIN VORTEX (Schriftfarben bitte in sattem Rot)
In der Mitte des Bildes soll das Maskottchen aufscheinen. (zähnefletschender Grizzly mit muskulösem Oberarm und Hantel in der Hand)
Hintergrundbild sollte blau bis dunkelblau/schwarz mit weißen/gelben Blitzen (Gewitter) gehalten sein!
Im unteren Bereich des Etiketts dann folgende Worte: (Linksseitig) Pre Workout Booster - Ultra concentrated, (rechtsseitig) 1 Serving = 20g, Net Wt. 400g
In meinem Anhang entnehmen Sie bitte ein ungefähres Beispiel Bild (ohne Aufschrift).

```html
<!DOCTYPE html>
<html lang="en">
<head>
<meta charset="utf-8">
<title>Marlin Vortex – Pre Workout Booster Label</title>
<link rel="stylesheet" href="https://fonts.googleapis.com/css2?family=Russo+One&family=Oswald:wght@600&family=Montserrat:wght@800&display=swap">
<style>
  :root {
    --page-bg: #f3f3f8;
    --label-navy: #1f3560;
    --label-navy-deep: #1a2d52;
    --brand-red: #dc2c44;
    --white: #ffffff;
    --lightning-light: #c9d3ea;
    --lightning-mid: #8e9bbb;
    --mascot-brown: #7a6750;
    --mascot-brown-deep: #5a4a38;
  }
  * { margin: 0; padding: 0; box-sizing: border-box; }
  html, body {
    width: 1200px;
    height: 869px;
    overflow: hidden;
    background: var(--page-bg);
  }
  .canvas {
    position: relative;
    width: 1200px;
    height: 869px;
  }
  .label {
    position: absolute;
    left: 330px;
    top: 50px;
    width: 540px;
    height: 770px;
    background: linear-gradient(180deg, var(--label-navy) 0%, var(--label-navy-deep) 100%);
    overflow: hidden;
  }
  .product-name {
    position: absolute;
    top: 40px;
    left: 0;
    right: 0;
    text-align: center;
    font-family: "Russo One", sans-serif;
    font-weight: 400;
    font-size: 74px;
    line-height: 0.92;
    color: var(--brand-red);
    letter-spacing: 1px;
  }
  .mascot-art {
    position: absolute;
    left: 90px;
    top: 225px;
    width: 380px;
    height: 410px;
    border-radius: 28px;
    background: linear-gradient(200deg,
      var(--lightning-light) 0%,
      var(--lightning-mid) 22%,
      var(--mascot-brown) 50%,
      var(--mascot-brown-deep) 100%);
  }
  .product-type {
    position: absolute;
    left: 30px;
    bottom: 26px;
    font-family: "Oswald", sans-serif;
    font-weight: 600;
    font-size: 26px;
    line-height: 1.0;
    color: var(--white);
    text-transform: uppercase;
  }
  .product-type span {
    display: inline-block;
    background: var(--brand-red);
    padding: 0 5px;
  }
  .product-amount {
    position: absolute;
    right: 26px;
    bottom: 70px;
    text-align: right;
    font-family: "Montserrat", sans-serif;
    font-weight: 800;
    color: var(--white);
  }
  .serving-size { font-size: 15px; letter-spacing: 0.5px; }
  .net-weight { font-size: 25px; margin-top: 2px; }
</style>
</head>
<body>
  <main class="canvas">
    <section class="label">
      <h1 class="product-name">MARLIN<br>VORTEX</h1>
      <div class="mascot-art" role="img" aria-label="Roaring grizzly bear mascot with muscular arms gripping a dumbbell, white lightning bolts striking behind it"></div>
      <p class="product-type"><span>Pre Workout Booster</span><br><span>Ultra Concentrated</span></p>
      <div class="product-amount">
        <p class="serving-size">1 Serving: 20 g</p>
        <p class="net-weight">400 g</p>
      </div>
    </section>
  </main>
</body>
</html>
```